Retail Cannabis Store Daily Promotions Graphic for Website/Social Media and Postcard

This project is for a business in Portland, Oregon called Marlow Leaf. We are a medical and recreational cannabis dispensary serving our neighborhoods since 2015. We would like to update some of our daily sales and need a new graphic to spread the word to the community. Ideally, we would like to use it on our social media, website and distribute it in our stores in the form of postcards.

It should be a simple run down of every day of the week and what promotions we have for that day. Additionally, we run a Veterans discount daily and would like to include a few calls to actions.

Target Market(s)

Cannabis users, adults between ages of 21 - 60.

Industry/Entity Type

Retail

Font styles to use
Other font styles liked:
• LetterGothicStd

Colors
aacf37
ffffff
9bcb3c
fcf9ce

Requirements
Must have
• I have attached our company logo files in ai format as well as our old daily deals graphic. For some additional color, we have been working towards revamping the feel of our brands and thus graphics. Attached you will see our latest designs (Attachments 4-6). We would like to follow a similar clean feel for the new daily deals graphic.
• Below is the language for the deals that need to be displayed on the graphic. The name of the deal (eg "Medible Monday") should be more prominent and the details that follow can be a bit more muted (possible suggestions: smaller font, under the deal name, etc) :
• Medible Monday - 15% Off All Edible Products
• $20 Tuesday - Select Flowers on Sale For $20/Eighth! (w/ tax)
• Topical Tuesday - 15% Off All Topical Products
• Waxy Wednesday - 15% Off All Concentrates, Extracts and Cartridges
• $30 Thursday - Select Top Shelf on Sale For $30/Eighth! (w/ tax)
• $1 Joint Friday - Get A 1/2g Joint for Just $1
• Shatterday - 15% Off All Concentrates, Extracts and Cartridges
• CBD Sunday - 15% Off All High CBD Products
• Veteran/Senior (65+) Receive 10% Discount Daily
• Ask About Our Neighborhood Discount Program
• Sign Up for Our Rewards Program And Start Saving
• Also, we need to include the following disclosure (can be in a smaller font, somewhere more discreet):
• "For use only by adults 21 years of age and older. Keep marijuana out of the reach of children. Do not operate a vehicle or machinery under the influence of this drug”

```html
<!DOCTYPE html>
<html lang="en">
<head>
<meta charset="utf-8">
<title>Marlow Leaf Daily Deals</title>
<link rel="stylesheet" href="https://fonts.googleapis.com/css2?family=Signika:wght@300;400&family=Share+Tech+Mono&display=swap">
<style>
  :root {
    --leaf-green: #9bcb3c;
    --lime: #aacf37;
    --paper: #ffffff;
    --cream: #fcf9ce;
    --muted: #8a8a8a;
  }
  * { margin: 0; padding: 0; box-sizing: border-box; }
  html, body { width: 750px; height: 1200px; overflow: hidden; background: var(--paper); }
  .deals-card {
    position: relative;
    width: 750px;
    height: 1200px;
    background: var(--paper);
    font-family: "Share Tech Mono", monospace;
    color: var(--muted);
  }
  .title {
    position: absolute;
    top: 48px; left: 0; right: 0;
    text-align: center;
    font-family: "Signika", sans-serif;
    font-weight: 300;
    font-size: 58px;
    letter-spacing: 10px;
    color: var(--leaf-green);
  }
  .rule {
    position: absolute;
    left: 45px; right: 45px;
    height: 3px;
    background: var(--leaf-green);
  }
  .rule--top { top: 130px; }
  .rule--bottom { top: 680px; }
  .deal-grid {
    position: absolute;
    top: 160px; left: 45px; right: 45px;
    display: grid;
    grid-template-columns: 1fr 1fr;
    grid-auto-rows: 132px;
  }
  .deal { text-align: center; }
  .deal__name {
    font-family: "Signika", sans-serif;
    font-weight: 400;
    font-size: 35px;
    color: var(--leaf-green);
    line-height: 1.1;
    margin-bottom: 14px;
  }
  .deal__detail {
    font-size: 20px;
    line-height: 1.35;
    letter-spacing: 0.5px;
  }
  .daily-discount {
    position: absolute;
    top: 703px; left: 0; right: 0;
    text-align: center;
    font-size: 20px;
    letter-spacing: 0.5px;
  }
  .rewards-band {
    position: absolute;
    top: 735px; left: 45px; right: 45px;
    height: 36px;
    background: var(--leaf-green);
    color: var(--paper);
    text-align: center;
    font-size: 21px;
    line-height: 36px;
    letter-spacing: 0.5px;
  }
  .brand {
    position: absolute;
    top: 810px; left: 0; right: 0;
    display: flex;
    align-items: center;
    justify-content: center;
    gap: 22px;
  }
  .brand__dot { width: 70px; height: 70px; }
  .brand__name {
    font-family: "Signika", sans-serif;
    font-weight: 400;
    font-size: 54px;
    letter-spacing: 3px;
    color: var(--muted);
  }
  .disclosure {
    position: absolute;
    top: 955px; left: 40px; right: 40px;
    text-align: center;
    font-size: 19px;
    line-height: 1.45;
    letter-spacing: 0.6px;
  }
</style>
</head>
<body>
<main class="deals-card">
  <h1 class="title">DAILY DEALS</h1>
  <div class="rule rule--top"></div>

  <section class="deal-grid">
    <article class="deal">
      <h2 class="deal__name">Medible Monday</h2>
      <p class="deal__detail">15% Off<br>All Edible Products</p>
    </article>
    <article class="deal">
      <h2 class="deal__name">$20 Tuesday</h2>
      <p class="deal__detail">Select Flowers on Sale<br>For $20/Eighth! (w/ tax)</p>
    </article>
    <article class="deal">
      <h2 class="deal__name">Topical Tuesday</h2>
      <p class="deal__detail">15% Off<br>All Topical Products</p>
    </article>
    <article class="deal">
      <h2 class="deal__name">Waxy Wednesday</h2>
      <p class="deal__detail">15% Off All Concentrates,<br>Extracts and Cartridges</p>
    </article>
    <article class="deal">
      <h2 class="deal__name">$30 Thursday</h2>
      <p class="deal__detail">Select Top Shelf on Sale<br>For $30/Eighth! (w/ tax)</p>
    </article>
    <article class="deal">
      <h2 class="deal__name">$1 Joint Friday</h2>
      <p class="deal__detail">Get A 1/2g Joint<br>for Just $1</p>
    </article>
    <article class="deal">
      <h2 class="deal__name">Shatterday</h2>
      <p class="deal__detail">15% Off All Concentrates,<br>Extracts and Cartridges</p>
    </article>
    <article class="deal">
      <h2 class="deal__name">CBD Sunday</h2>
      <p class="deal__detail">15% Off<br>All High CBD Products</p>
    </article>
  </section>

  <div class="rule rule--bottom"></div>
  <p class="daily-discount">Veteran/Senior (65+) Receive 10% Discount Daily</p>
  <p class="rewards-band">Sign Up for Our Rewards Program And Start Saving</p>

  <div class="brand">
    <svg class="brand__dot" viewBox="0 0 70 70" aria-hidden="true">
      <circle cx="35" cy="35" r="33" fill="var(--leaf-green)"/>
    </svg>
    <span class="brand__name">MARLOW LEAF</span>
  </div>

  <p class="disclosure">For use only by adults 21 years of age and older.<br>Keep marijuana out of the reach of children. Do not operate<br>a vehicle or machinery under the influence of this drug</p>
</main>
</body>
</html>
```